Business Card Design using new logo

As much as we'd like to think that treating everyone equally is the best strategy for fairness, the reality is that the differences in the lives of women and men have to be taken into account to ensure that organizations, programs, services, and yes, even public policy treat women and men in ways that achieve gender equity.

That's where ParityLoom - balance insight metrics comes in. Using the data-driven tools of gender analysis, our organization can help anyone determine if gender equity is being achieved - in businesses and organizations, in the planning and implementation of programs and services, and in the development and enforcement of public policy.
Updates

Apologies for the delay - have not had time to finalize the decision.  Should be early this week - probably Tuesday.

Industry/Entity Type

Business

Requirements
Must have
• New Logo for ParityLoom
• Logo plus words "Balance Insight Metrics"

```html
<!DOCTYPE html>
<html lang="en">
<head>
<meta charset="utf-8">
<title>ParityLoom Business Card</title>
<link rel="stylesheet" href="https://fonts.googleapis.com/css2?family=Open+Sans:wght@400;600;700&display=swap">
<style>
  :root {
    --bg: #ecebe8;
    --card-dark: #231f20;
    --card-white: #ffffff;
    --accent: #f7941d;
    --silver: #bcbdc0;
    --ink: #2b2b2b;
    --text-light: #e6e6e6;
    --text-muted: #9a9a9a;
  }
  * { box-sizing: border-box; margin: 0; padding: 0; }
  html, body { width: 1200px; height: 1024px; overflow: hidden; }
  body {
    background: var(--bg);
    font-family: "Open Sans", Arial, sans-serif;
    position: relative;
  }
  .card {
    position: absolute;
    left: 250px;
    width: 700px;
    height: 400px;
    border-radius: 24px;
    overflow: hidden;
    background: var(--card-dark);
    box-shadow: 0 10px 30px rgba(0,0,0,0.18);
  }
  .card--front { top: 70px; }
  .card--back { top: 554px; }
  .card__shapes { position: absolute; inset: 0; width: 100%; height: 100%; }

  .brand {
    position: absolute;
    display: flex;
    align-items: center;
    gap: 14px;
  }
  .brand__dot {
    border-radius: 50%;
    background: var(--accent);
    flex: none;
  }
  .brand__text { display: flex; flex-direction: column; }
  .brand__name { font-weight: 600; letter-spacing: -0.5px; line-height: 1.1; }
  .brand__tagline { font-weight: 400; letter-spacing: 1px; text-transform: uppercase; }

  .card--front .brand { left: 40px; top: 70px; }
  .card--front .brand__dot { width: 36px; height: 36px; }
  .card--front .brand__name { font-size: 44px; color: var(--ink); }
  .card--front .brand__tagline { font-size: 11px; color: var(--text-muted); margin-top: 2px; }

  .holder { position: absolute; left: 150px; top: 318px; }
  .holder__name { color: var(--accent); font-weight: 700; font-size: 20px; letter-spacing: 0.5px; }
  .holder__title { color: var(--text-muted); font-size: 16px; margin-top: 2px; }

  .divider {
    position: absolute;
    left: 330px; top: 262px;
    width: 70px; height: 2px;
    background: linear-gradient(90deg, transparent, var(--accent), transparent);
  }

  .contacts {
    position: absolute;
    right: 34px; top: 214px;
    list-style: none;
    text-align: right;
  }
  .contacts li {
    display: flex;
    justify-content: flex-end;
    align-items: center;
    gap: 10px;
    color: var(--text-light);
    font-size: 16px;
    line-height: 25px;
  }
  .contacts svg { width: 14px; height: 14px; flex: none; }

  .card--back .brand {
    left: 0; right: 0; top: 118px;
    justify-content: center;
  }
  .card--back .brand__dot { width: 58px; height: 58px; }
  .card--back .brand__name { font-size: 72px; color: var(--card-white); }
  .card--back .brand__tagline { font-size: 15px; color: var(--silver); margin-top: 2px; letter-spacing: 2px; }
  .website {
    position: absolute;
    left: 0; right: 0; top: 262px;
    text-align: center;
    color: var(--accent);
    font-size: 22px;
    letter-spacing: 0.5px;
  }
</style>
</head>
<body>

<section class="card card--front">
  <svg class="card__shapes" viewBox="0 0 700 400" aria-hidden="true">
    <path d="M0,0 H470 C420,120 330,230 0,272 Z" fill="var(--card-white)"/>
    <path d="M0,272 C330,230 420,120 470,0 H488 C446,140 356,252 0,304 Z" fill="var(--silver)"/>
    <path d="M500,0 H566 C524,94 456,170 378,214 C444,152 482,80 500,0 Z" fill="var(--accent)"/>
  </svg>

  <div class="brand">
    <span class="brand__dot"></span>
    <div class="brand__text">
      <span class="brand__name">ParityLoom</span>
      <span class="brand__tagline">Balance Insight Metrics</span>
    </div>
  </div>

  <div class="divider"></div>

  <div class="holder">
    <p class="holder__name">MARCUS HALE</p>
    <p class="holder__title">Job Title</p>
  </div>

  <ul class="contacts">
    <li>000.000.0000
      <svg viewBox="0 0 14 14"><path d="M3 1 L5.5 1 L6.5 4 L5 5.2 C5.8 7 7 8.2 8.8 9 L10 7.5 L13 8.5 L13 11 C13 12 12 13 11 13 C5.5 13 1 8.5 1 3 C1 2 2 1 3 1 Z" fill="var(--accent)"/></svg>
    </li>
    <li>000.000.0000
      <svg viewBox="0 0 14 14"><rect x="3" y="1" width="8" height="12" rx="1.5" fill="none" stroke="var(--accent)" stroke-width="1.6"/></svg>
    </li>
    <li>parityloom.com
      <svg viewBox="0 0 14 14"><circle cx="7" cy="7" r="5.8" fill="none" stroke="var(--accent)" stroke-width="1.5"/><path d="M1.5 7 H12.5 M7 1.2 C4.5 4 4.5 10 7 12.8 M7 1.2 C9.5 4 9.5 10 7 12.8" fill="none" stroke="var(--accent)" stroke-width="1.1"/></svg>
    </li>
    <li>@ParityLoom
      <svg viewBox="0 0 14 14"><rect x="1" y="1" width="12" height="12" rx="2" fill="var(--accent)"/></svg>
    </li>
    <li>email@parityloom.com
      <svg viewBox="0 0 14 14"><rect x="1" y="3" width="12" height="8" fill="var(--accent)"/><path d="M1 3 L7 8 L13 3" fill="none" stroke="var(--card-dark)" stroke-width="1.2"/></svg>
    </li>
  </ul>
</section>

<section class="card card--back">
  <div class="brand">
    <span class="brand__dot"></span>
    <div class="brand__text">
      <span class="brand__name">ParityLoom</span>
      <span class="brand__tagline">Balance Insight Metrics</span>
    </div>
  </div>
  <p class="website">www.parityloom.com</p>
</section>

</body>
</html>
```